Travel Agency Website - Simple General

Need a 7 page simple design that is pretty repetitive. Need to be able to load quickly that is SEO optimized. Trying to give ideas on what they can do, be personal as we are local, but at the same time come across as professional and get information easily with little burden.

- Landing Page
- Brambleton Vacations Page
- Family Trips
- Road Trips from Texas
- Other Destinations
- About Us Page
- Contact Us Page

Target Market(s)

Families

Coding

Coded - Design and coding required

Number of Pages Required

5+ page

Colors

Designer to choose colors to be used in the design.

Requirements
Must have
• Like it to flow easily with our logo. Use that for colors, etc.

```html
<!DOCTYPE html>
<html lang="en">
<head>
<meta charset="utf-8">
<title>About Us – Meander Lane Travel Co.</title>
<link href="https://fonts.googleapis.com/css2?family=Barlow+Condensed:wght@500;600&family=Outfit:wght@300;400;500&display=swap" rel="stylesheet">
<style>
  :root{
    --ink:#0f3d4c;
    --teal:#2f857f;
    --gold:#c69449;
    --bg:#e9eee7;
    --bg-soft:#eef1ec;
    --card:#eef1ed;
    --text:#2d4d58;
  }
  *{box-sizing:border-box;margin:0;padding:0}
  html,body{width:1200px;height:1027px;overflow:hidden}
  body{background:var(--bg);font-family:'Outfit',sans-serif;color:var(--text);position:relative}
  .backdrop{position:absolute;inset:0;
    background:
      radial-gradient(ellipse 260px 420px at 90px 700px, rgba(170,150,120,.35), transparent 70%),
      radial-gradient(ellipse 240px 300px at 1080px 760px, rgba(150,175,120,.3), transparent 70%),
      linear-gradient(180deg,#eaeee8 0%,#e6ebe3 60%,#e8ece5 100%);}
  .footer-band{position:absolute;left:0;right:0;top:825px;bottom:0;background:rgba(240,243,238,.55)}
  .site-header{position:absolute;top:0;left:0;right:0;height:120px}
  .brand{position:absolute;left:125px;top:40px;display:flex;align-items:center;gap:8px;
    font-family:'Outfit',sans-serif;font-weight:500;font-size:15px;color:var(--ink)}
  .brand-dot{width:14px;height:14px;border-radius:50%;background:var(--teal)}
  .main-nav{position:absolute;top:52px;right:126px;display:flex;gap:24px;font-size:10.5px;color:var(--ink)}
  .main-nav a{color:inherit;text-decoration:none}
  h1,h2,.card-title{font-family:'Barlow Condensed',sans-serif;font-weight:600;color:var(--ink)}
  .accent{color:var(--teal)}
  .page-title{position:absolute;top:166px;left:0;right:0;text-align:center;font-size:54px;line-height:1;letter-spacing:-.5px}
  .page-sub{position:absolute;top:237px;left:0;right:0;text-align:center;font-size:13.5px;color:#3f5a62}
  .cards{position:absolute;top:273px;left:247px;display:flex;gap:10px}
  .card{width:229px;height:266px;background:var(--card);border-radius:14px;padding:4px 5px;
    box-shadow:0 8px 24px rgba(60,80,70,.08)}
  .card-photo{height:200px;border-radius:11px 11px 0 0;position:relative;overflow:hidden}
  .card-photo::after{content:"";position:absolute;left:0;right:0;bottom:0;height:70px;
    background:linear-gradient(180deg,transparent,var(--card))}
  .photo-family{background:linear-gradient(160deg,#6f98c0 0%,#c9a58a 45%,#4a3a30 100%)}
  .photo-park{background:linear-gradient(160deg,#f1f1ec 0%,#e6d48a 45%,#5d7fa8 100%)}
  .photo-road{background:linear-gradient(160deg,#3f6b2a 0%,#7fa24a 50%,#d5dac8 100%)}
  .card-title{text-align:center;font-size:19px;margin-top:-18px;position:relative}
  .who{position:absolute;top:632px;left:280px;width:640px;text-align:center}
  .who h2{font-size:37px;line-height:1;margin-bottom:16px}
  .who p{font-size:11.6px;line-height:17.5px;margin-bottom:7px;color:#33535d}
  .contact-row{position:absolute;top:912px;left:0;right:0}
  .contact{position:absolute;display:flex;align-items:center;gap:11px}
  .icon-circle{width:48px;height:48px;border-radius:50%;background:var(--gold);display:flex;align-items:center;justify-content:center}
  .contact small{display:block;font-size:10px;font-weight:500;color:var(--ink)}
  .contact span{font-size:13px;color:var(--ink)}
  .social{position:absolute;top:12px;display:flex;align-items:center;gap:7px;font-size:10.5px;color:var(--ink);text-decoration:underline}
  .social i{width:26px;height:26px;border-radius:50%;background:var(--gold);display:block}
</style>
</head>
<body>
  <div class="backdrop" role="img" aria-label="Soft faded photo of travellers in sun hats reading a map outdoors"></div>
  <div class="footer-band"></div>

  <header class="site-header">
    <div class="brand"><span class="brand-dot"></span>Meander Lane Travel Co.</div>
    <nav class="main-nav">
      <a href="#">Home</a><a href="#">Brambleton Vacations</a><a href="#">Family Trips</a>
      <a href="#">Texas Road Trips</a><a href="#">Other Destinations</a><a href="#">About Us</a><a href="#">Contact</a>
    </nav>
  </header>

  <h1 class="page-title">About Our <span class="accent">Family</span></h1>
  <p class="page-sub">Creating unforgettable travel experiences for families like yours</p>

  <section class="cards">
    <article class="card"><div class="card-photo photo-family" role="img" aria-label="Smiling family on a seaside promenade"></div><h3 class="card-title">Family Travel</h3></article>
    <article class="card"><div class="card-photo photo-park" role="img" aria-label="Woman riding a carousel at a theme park"></div><h3 class="card-title">Brambleton Trip</h3></article>
    <article class="card"><div class="card-photo photo-road" role="img" aria-label="Jeep driving along a green forest road"></div><h3 class="card-title">Road Trip</h3></article>
  </section>

  <section class="who">
    <h2>Who <span class="accent">We</span> Are</h2>
    <p>We are a family-focused travel planning service dedicated to helping families create stress-free and memorable vacations. From magical Brambleton experiences to relaxing family beach trips and exciting road adventures across Texas, we handle all the planning so you can focus on making memories.</p>
    <p>Our goal is simple — make travel easy, personal, and enjoyable for every family. We believe every trip should feel special, no matter the budget or destination.</p>
  </section>

  <footer class="contact-row">
    <div class="contact" style="left:239px">
      <div class="icon-circle"><svg width="18" height="18" viewBox="0 0 24 24"><path fill="#fff" d="M6.6 10.8a15.1 15.1 0 0 0 6.6 6.6l2.2-2.2a1 1 0 0 1 1-.25 11.4 11.4 0 0 0 3.6.57 1 1 0 0 1 1 1V20a1 1 0 0 1-1 1A17 17 0 0 1 3 4a1 1 0 0 1 1-1h3.5a1 1 0 0 1 1 1c0 1.25.2 2.45.57 3.57a1 1 0 0 1-.25 1z"/></svg></div>
      <div><small>Call Us:</small><span>555.014.2290</span></div>
    </div>
    <div class="contact" style="left:418px">
      <div class="icon-circle"><svg width="18" height="14" viewBox="0 0 20 14"><rect width="20" height="14" rx="2" fill="#fff"/><path d="M1 1l9 7 9-7" stroke="#c69449" stroke-width="1.6" fill="none"/></svg></div>
      <div><small>Email Address:</small><span>hello@meanderlanetravel.com</span></div>
    </div>
    <a class="social" style="left:760px"><i></i>Friends Page</a>
    <a class="social" style="left:880px"><i></i>Photo Feed</a>
  </footer>
</body>
</html>
```